Corporate Web Redesign Project - coded

We would like redesign/refresh of our current site that would allow us to increase the depth of content and create a high quality impression for visitors.

Current site - http://corvanisystems.example/

A previous web redesign project has improved our site but it has not really reached the level we require.

Our customers are global, blue chip, organisations and a professional, corporate style of site is required.

Please note we would prefer a coded website to a just a design. We are happy to provide a zip of our current site if required.
Updates

                                   

Target Market(s)

Global oil and gas producers, KT, Pardo, Valmira etc.

Industry/Entity Type

It Professional

Requirements
Must have
• Design should support the level of content we currently have in the existing sitemap - although it should be expandable a site design for a large / complex site would not be appropriate

All current content / pages to be reflected in design

Must be visually appealing

Intuitive and clear navigation that is expandable

Display a high level of professionalism

Use a consistent palette of colours that complements our logo

Clean and organized layout

A way to capture visitor’s information or Call to action (i.e. contact link or form) on every page

Prominent Contact Information
Should not have
• Flash

```html
<!DOCTYPE html>
<html lang="en">
<head>
<meta charset="utf-8">
<title>Corvani Systems — The Business of Drilling Wells</title>
<link href="https://fonts.googleapis.com/css2?family=PT+Sans&family=Arimo:wght@700&display=swap" rel="stylesheet">
<style>
  :root {
    --ink-teal: #244848;
    --brand-teal: #2f6b72;
    --nav-text: #6a6a6a;
    --nav-active: #2a2a2a;
    --rule: #cfcfcf;
    --hero-bg: #f8f8f8;
    --page-bg: #ffffff;
  }
  * { box-sizing: border-box; margin: 0; padding: 0; }
  html, body { width: 1200px; height: 558px; overflow: hidden; background: var(--page-bg); }
  .page { position: relative; width: 1200px; height: 558px; overflow: hidden; font-family: "PT Sans", sans-serif; }

  .brand { position: absolute; left: 123px; top: 66px; display: flex; align-items: center; gap: 10px; }
  .brand-dot { width: 22px; height: 22px; border-radius: 50%; background: var(--brand-teal); }
  .brand-name { font-family: "PT Sans", sans-serif; font-size: 24px; color: var(--ink-teal); letter-spacing: 0.5px; }

  .account-links { position: absolute; right: 111px; top: 83px; font-size: 12.5px; color: var(--nav-text); display: flex; gap: 10px; }
  .account-links a { color: inherit; text-decoration: none; }
  .account-links .sep { color: #8aa; }

  .main-nav { position: absolute; left: 659px; top: 151px; display: flex; border: 1px solid var(--rule); height: 43px; }
  .main-nav a { display: flex; align-items: center; padding: 0 19.5px; font-size: 12px; color: var(--nav-text); text-decoration: none; border-left: 1px solid var(--rule); }
  .main-nav a:first-child { border-left: none; }
  .main-nav a.is-active { background: #f6f6f6; color: var(--nav-active); }

  .header-rule { position: absolute; left: 113px; top: 193px; width: 974px; height: 1px; background: var(--rule); }

  .hero { position: absolute; left: 33px; top: 228px; width: 1127px; height: 330px;
    background: linear-gradient(90deg, var(--hero-bg) 0%, var(--hero-bg) 60%, #ffffff 100%); }
  .hero-visual { position: absolute; z-index: 0; left: 740px; top: 30px; width: 380px; height: 300px;
    background: radial-gradient(ellipse at 50% 60%, #d2d2d2 0%, #e6e6e6 40%, rgba(255,255,255,0) 70%); }
  .hero-title { position: absolute; z-index: 1; left: 18px; top: 106px; font-family: "Arimo", sans-serif; font-weight: 700; font-size: 34px; color: var(--ink-teal); letter-spacing: -0.3px; }
  .hero-points { position: absolute; z-index: 1; left: 30px; top: 157px; list-style: none; }
  .hero-points li { display: flex; align-items: center; height: 53.5px; font-family: "Arimo", sans-serif; font-weight: 700; font-size: 27px; color: var(--ink-teal); letter-spacing: -0.3px; white-space: nowrap; }
  .hero-points svg { width: 19px; height: 26px; margin-right: 24px; flex: none; }
</style>
</head>
<body>
<div class="page">
  <header>
    <div class="brand">
      <span class="brand-dot"></span>
      <span class="brand-name">CORVANI SYSTEMS</span>
    </div>
    <div class="account-links"><a href="#">LOG IN</a><span class="sep">|</span><a href="#">SIGN UP</a></div>
    <nav class="main-nav">
      <a href="#" class="is-active">HOME</a>
      <a href="#">NEWS</a>
      <a href="#">ABOUT US</a>
      <a href="#">SOLUTIONS</a>
      <a href="#">CONTACT</a>
    </nav>
    <div class="header-rule"></div>
  </header>

  <section class="hero">
    <div class="hero-visual" role="img" aria-label="Illustration of an offshore jack-up drilling rig with cranes and derricks"></div>
    <h1 class="hero-title">The Business of Drilling Wells</h1>
    <ul class="hero-points">
      <li><svg viewBox="0 0 19 26"><path d="M9.5 1 C12 8 18 13 18 18 A8.5 8 0 0 1 1 18 C1 13 7 8 9.5 1 Z" fill="var(--ink-teal)"/></svg>Understand and communicate project cost and risk</li>
      <li><svg viewBox="0 0 19 26"><path d="M9.5 1 C12 8 18 13 18 18 A8.5 8 0 0 1 1 18 C1 13 7 8 9.5 1 Z" fill="var(--ink-teal)"/></svg>Control and reduce expenditure</li>
      <li><svg viewBox="0 0 19 26"><path d="M9.5 1 C12 8 18 13 18 18 A8.5 8 0 0 1 1 18 C1 13 7 8 9.5 1 Z" fill="var(--ink-teal)"/></svg>Learn and improve performance</li>
    </ul>
  </section>
</div>
</body>
</html>
```